Harbourline Estate Group

The card is to be black

On the front it will say "Harbourline"
And just under it in smaller writing "Property Group" in dark brown or rose gold

Daniel Forsett
0471 586 209
Admin@harblinegroup.example

On the back it is to say Harbourline Estate group same style as the front but smaller.
And then under that say:
Electrical
General Maintenance
Building works & construction
Energy Consulants

Target Market(s)

Re

Industry/Entity Type

Electrical

Contact Information for Business Card

The card is to be black

Daniel Forsett
0471 586 209
Admin@harblinegroup.example

And then under that say:
Electrical
General Maintenance
Energy Consulants

And somewhere else put residential domestic and industrial

Font styles to use
Serif

Requirements
Should not have
• No pictures of tools etc just a plain sleek card

```html
<!DOCTYPE html>
<html lang="en">
<head>
<meta charset="utf-8">
<title>Harbourline Estate Group — Business Card</title>
<link rel="stylesheet" href="https://fonts.googleapis.com/css2?family=Lato:wght@400;700;900&display=swap">
<style>
  :root {
    --stage: #3a3a3a;
    --card-top: #333334;
    --card-bottom: #222223;
    --ink-light: #f2f2f2;
    --ink-soft: #d9d9d9;
    --rose: #b8677a;
    --rose-deep: #9c5064;
  }
  * { box-sizing: border-box; margin: 0; padding: 0; }
  html, body {
    width: 1200px; height: 873px; overflow: hidden;
    background: var(--stage);
    font-family: "Lato", Arial, sans-serif;
  }
  .stage {
    position: relative; width: 1200px; height: 873px;
    display: flex; align-items: center; justify-content: center; gap: 40px;
  }
  .card {
    position: relative; width: 540px; height: 309px;
    border-radius: 16px; overflow: hidden;
    box-shadow: 0 14px 30px rgba(0,0,0,.45);
  }
  .card__texture {
    position: absolute; inset: 0;
    background: linear-gradient(150deg, var(--card-top) 0%, #2a2a2b 45%, var(--card-bottom) 100%);
  }
  .brand { position: absolute; left: 0; right: 0; text-align: center; }
  .brand__name {
    color: var(--ink-light); font-weight: 900; text-transform: uppercase;
    letter-spacing: .5px; line-height: 1;
  }
  .brand__tagline {
    color: var(--rose); font-weight: 700; text-transform: uppercase;
    letter-spacing: 5px; line-height: 1;
  }

  /* Back */
  .card--back .brand { top: 52px; }
  .card--back .brand__name { font-size: 40px; }
  .card--back .brand__tagline { font-size: 12px; margin-top: 6px; letter-spacing: 4px; }
  .services-rule {
    position: absolute; left: 36px; right: 36px; top: 150px;
    display: flex; align-items: center; gap: 12px;
  }
  .services-rule::before, .services-rule::after {
    content: ""; flex: 1; height: 1px; background: var(--rose-deep);
  }
  .services-rule__label {
    color: var(--ink-light); font-weight: 700; font-size: 15px; letter-spacing: .5px;
  }
  .services {
    position: absolute; top: 178px; left: 110px; right: 60px;
    display: grid; grid-template-columns: 1fr 1fr; row-gap: 10px; column-gap: 30px;
    list-style: none;
  }
  .services li {
    color: var(--ink-soft); font-size: 14px; display: flex; align-items: center; gap: 9px;
  }
  .services li::before {
    content: ""; width: 6px; height: 6px; border-radius: 50%; background: var(--rose);
  }

  /* Front */
  .card--front .brand { top: 56px; }
  .card--front .brand__name { font-size: 50px; }
  .card--front .brand__tagline { font-size: 15px; margin-top: 8px; }
  .person {
    position: absolute; left: 60px; top: 210px; text-align: right; width: 180px;
  }
  .person__name { color: var(--ink-light); font-weight: 900; font-size: 17px; letter-spacing: .3px; }
  .person__role { color: var(--rose); font-size: 16px; margin-top: 4px; }
  .divider {
    position: absolute; left: 262px; top: 178px; width: 2px; height: 86px;
    background: linear-gradient(to bottom, transparent, var(--rose), transparent);
  }
  .contacts { position: absolute; left: 286px; top: 184px; list-style: none; }
  .contacts li {
    display: flex; align-items: center; gap: 10px;
    color: var(--ink-soft); font-size: 15px; margin-bottom: 12px;
  }
  .contacts svg { width: 17px; height: 14px; fill: var(--rose); flex: none; }
</style>
</head>
<body>
<main class="stage">

  <section class="card card--back" aria-label="Card back">
    <div class="card__texture" role="img" aria-label="Dark faceted polygon texture"></div>
    <div class="brand">
      <div class="brand__name">Harbourline</div>
      <div class="brand__tagline">Property Group</div>
    </div>
    <div class="services-rule"><span class="services-rule__label">OUR SERVICES</span></div>
    <ul class="services">
      <li>Electrical</li>
      <li>Energy Consulants</li>
      <li>General Maintenance</li>
      <li>Building works &amp; construction</li>
    </ul>
  </section>

  <section class="card card--front" aria-label="Card front">
    <div class="card__texture" role="img" aria-label="Dark faceted polygon texture"></div>
    <div class="brand">
      <div class="brand__name">Harbourline</div>
      <div class="brand__tagline">Property Group</div>
    </div>
    <div class="person">
      <div class="person__name">DANIEL FORSETT</div>
      <div class="person__role">Director</div>
    </div>
    <div class="divider"></div>
    <ul class="contacts">
      <li>
        <svg viewBox="0 0 17 14" aria-hidden="true"><path d="M1 4c0-2 3-3 7.5-3S16 2 16 4v1.5h-3.5V4H4.5v1.5H1z"/><path d="M3 7h11l1 6H2z"/></svg>
        0471 586 209
      </li>
      <li>
        <svg viewBox="0 0 17 14" aria-hidden="true"><path d="M1 1h15v12H1z M2.5 2.5 8.5 8l6-5.5" fill="none" stroke="#b8677a" stroke-width="1.6"/></svg>
        Admin@harblinegroup.example
      </li>
    </ul>
  </section>

</main>
</body>
</html>
```